Law practice business card

I have an existing logo that I would like to make a little cleaner and maybe something more creative, but using the same base. I would like a contempoary design of the business card.

Industry/Entity Type

Law

Logo Text

On one side of the card - below the logo - I would want to say "TOSPRAVO" and below that it should read "LAW OFFICES, PC" in smaller print. If you have somethign more creative, I would love to see it.

Logo styles of interest
Lettermark Logo
Font styles to use
Sans Serif

Colors

Designer to choose only greyscale colors for use in the design.

Requirements
Must have
• Standard info: My name with "Attorney at Law" underneath; phone, fax, address, email and website.

```html
<!DOCTYPE html>
<html lang="en">
<head>
<meta charset="utf-8">
<title>Tospravo Law Offices – Business Card</title>
<link href="https://fonts.googleapis.com/css2?family=Montserrat:wght@500;600&family=Open+Sans:wght@400;600&display=swap" rel="stylesheet">
<style>
  :root {
    --stage: #e9eaec;
    --paper: #ffffff;
    --ink: #1c1c1c;
    --mark-grey: #6e6e6e;
    --mark-light: #b4b4b4;
    --bar-grey: #bfc0c2;
    --back-dark: #2f3033;
    --back-mid: #55575a;
    --icon-grey: #8a8a8a;
    --panel-grey: #767676;
    --white: #ffffff;
  }
  * { margin: 0; padding: 0; box-sizing: border-box; }
  html, body { width: 1200px; height: 1200px; overflow: hidden; }
  body { position: relative; background: var(--stage); font-family: "Open Sans", Arial, sans-serif; }

  .stage { position: absolute; left: 0; top: 0; width: 1200px; height: 683px; background: var(--stage); }

  .card {
    position: absolute; top: 198px; width: 500px; height: 286px; overflow: hidden;
    box-shadow: 0 6px 18px rgba(0,0,0,.18);
  }
  .card--front { left: 60px; background: var(--paper); }
  .card--back { left: 640px; background: linear-gradient(135deg, var(--back-dark) 0%, var(--back-mid) 100%); }

  /* Wordmark: name on top, rule + tagline below spanning the same width */
  .wordmark { display: inline-block; font-family: "Montserrat", Arial, sans-serif; font-weight: 500; line-height: 1; }
  .wordmark__name { display: block; white-space: nowrap; }
  .wordmark__tag-row { display: flex; align-items: center; margin-top: 8px; }
  .wordmark__rule { flex: 1; height: 2px; margin-right: 10px; }
  .wordmark__tag { white-space: nowrap; }

  /* Front */
  .card--front .bar-top { position: absolute; left: 0; top: 22px; }
  .holder { position: absolute; left: 104px; top: 18px; }
  .holder__name { font-family: "Montserrat", Arial, sans-serif; font-weight: 600; font-size: 16px; color: var(--ink); letter-spacing: .5px; }
  .holder__role { font-size: 13px; color: var(--mark-grey); margin-top: 2px; }
  .contact { position: absolute; left: 26px; top: 84px; list-style: none; }
  .contact li { display: flex; align-items: flex-start; font-size: 12px; color: var(--ink); line-height: 18px; }
  .contact svg { width: 12px; height: 12px; margin: 3px 10px 0 0; flex: none; }
  .contact .no-icon { padding-left: 22px; }
  .card--front .wordmark { position: absolute; right: 26px; top: 176px; color: var(--mark-grey); }
  .card--front .wordmark__name { font-size: 32px; letter-spacing: 3px; }
  .card--front .wordmark__tag { font-size: 13px; letter-spacing: 2px; color: var(--ink); }
  .card--front .wordmark__rule { background: var(--ink); }
  .card--front .bar-bottom { position: absolute; right: 0; bottom: 16px; }

  /* Back */
  .card--back .wordmark { position: absolute; left: 50%; top: 84px; transform: translateX(-50%); color: var(--mark-light); }
  .card--back .wordmark__name { font-size: 46px; letter-spacing: 5px; }
  .card--back .wordmark__tag { font-size: 18px; letter-spacing: 3px; }
  .card--back .wordmark__rule { background: var(--mark-light); }
  .card--back .web { position: absolute; left: 0; right: 0; bottom: 40px; text-align: center; color: var(--mark-light); font-size: 16px; }

  /* Logo panels */
  .logo-panel { position: absolute; top: 683px; width: 600px; height: 517px; display: flex; align-items: center; justify-content: center; }
  .logo-panel--light { left: 0; background: var(--white); }
  .logo-panel--dark { left: 600px; background: var(--panel-grey); }
  .logo-panel .wordmark__name { font-size: 62px; letter-spacing: 6px; }
  .logo-panel .wordmark__tag-row { margin-top: 12px; }
  .logo-panel .wordmark__tag { font-size: 28px; letter-spacing: 4px; }
  .logo-panel .wordmark__rule { margin-right: 12px; }
  .logo-panel--light .wordmark { color: var(--mark-grey); }
  .logo-panel--light .wordmark__tag { color: var(--ink); }
  .logo-panel--light .wordmark__rule { background: var(--ink); }
  .logo-panel--dark .wordmark { color: var(--white); }
  .logo-panel--dark .wordmark__rule { background: var(--white); }
</style>
</head>
<body>
  <section class="stage">
    <article class="card card--front">
      <svg class="bar-top" width="90" height="26" viewBox="0 0 90 26">
        <polygon points="0,0 66,0 56,26 0,26" fill="var(--bar-grey)"/>
        <polygon points="72,0 90,0 80,26 62,26" fill="var(--mark-grey)"/>
      </svg>
      <div class="holder">
        <p class="holder__name">Marta Kovar</p>
        <p class="holder__role">Attorney at Law</p>
      </div>
      <ul class="contact">
        <li><svg viewBox="0 0 12 12"><path d="M6 1a3.5 3.5 0 0 1 3.5 3.5C9.5 7 6 11 6 11S2.5 7 2.5 4.5A3.5 3.5 0 0 1 6 1z" fill="none" stroke="var(--icon-grey)" stroke-width="1.2"/></svg>Lindenweg 8</li>
        <li class="no-icon">10115 Musterstadt</li>
        <li><svg viewBox="0 0 12 12"><path d="M3 1l2 2.5-1.2 1.3a6 6 0 0 0 3.4 3.4L8.5 7 11 9l-1.5 2C5 11 1 7 1 2.5z" fill="none" stroke="var(--icon-grey)" stroke-width="1.1"/></svg>+49 1111 5550102</li>
        <li><svg viewBox="0 0 12 12"><rect x="2" y="1" width="8" height="10" fill="none" stroke="var(--icon-grey)" stroke-width="1.1"/><path d="M4 4h4M4 6h4M4 8h2" stroke="var(--icon-grey)" stroke-width="1"/></svg>Fax +49 1111 5550103</li>
        <li><svg viewBox="0 0 12 12"><rect x="1" y="2.5" width="10" height="7" fill="none" stroke="var(--icon-grey)" stroke-width="1.1"/><path d="M1 2.5l5 4 5-4" fill="none" stroke="var(--icon-grey)" stroke-width="1.1"/></svg>office@tospravolaw.com</li>
        <li><svg viewBox="0 0 12 12"><circle cx="6" cy="6" r="4.5" fill="none" stroke="var(--icon-grey)" stroke-width="1.1"/><path d="M1.5 6h9M6 1.5c-2 2.5-2 6.5 0 9M6 1.5c2 2.5 2 6.5 0 9" fill="none" stroke="var(--icon-grey)" stroke-width="0.9"/></svg>www.tospravolaw.com</li>
      </ul>
      <div class="wordmark">
        <span class="wordmark__name">TOSPRAVO</span>
        <span class="wordmark__tag-row"><span class="wordmark__rule"></span><span class="wordmark__tag">LAW OFFICES</span></span>
      </div>
      <svg class="bar-bottom" width="190" height="20" viewBox="0 0 190 20">
        <polygon points="10,0 120,0 112,20 0,20" fill="var(--bar-grey)"/>
        <polygon points="128,0 190,0 190,20 120,20" fill="var(--mark-grey)"/>
      </svg>
    </article>

    <article class="card card--back">
      <div class="wordmark">
        <span class="wordmark__name">TOSPRAVO</span>
        <span class="wordmark__tag-row"><span class="wordmark__rule"></span><span class="wordmark__tag">LAW OFFICES</span></span>
      </div>
      <p class="web">www.tospravolaw.com</p>
    </article>
  </section>

  <section class="logo-panel logo-panel--light">
    <div class="wordmark">
      <span class="wordmark__name">TOSPRAVO</span>
      <span class="wordmark__tag-row"><span class="wordmark__rule"></span><span class="wordmark__tag">LAW OFFICES</span></span>
    </div>
  </section>
  <section class="logo-panel logo-panel--dark">
    <div class="wordmark">
      <span class="wordmark__name">TOSPRAVO</span>
      <span class="wordmark__tag-row"><span class="wordmark__rule"></span><span class="wordmark__tag">LAW OFFICES</span></span>
    </div>
  </section>
</body>
</html>
```